依頼詳細
フリーペーパーに載せるための営業広告のデザインをお願いします。A6の用紙1ページのカラーです。1ページなのですが、上半分はミントリーフオオサカの紹介、下半分は管楽器修理工房高槻の広告として使いたいです。
記載項目
上半分
ミントリーフオオサカ
2012年5月オープン予定!
・東京都新宿区大久保の地下に隠れ家的楽器店
・リペアマン常在
・中古楽器買取強化実施中!
・委託も歓迎
・レアアイテムもあるよ!
169-0052
東京都新宿区北新宿5-8-6
リバティ西新宿ビル地下1階
電話番号、アドレス等準備中!

下半分
管楽器修理工房 高槻
・誠実一路!
・街中にある楽器屋!
・高い技術とリーズナブルな価格設定。
・メッキのかけなおし、ラッカー剥離の特殊修理もお任せください
・中古・新品とも販売中!
・どんな状態の楽器でも買い取ります!

技術者紹介
・平成12年、高校卒業後、名古屋の専門学校で楽器修理技術を学ぶ。
・専門学校卒業後、ノルウェーの大学KRS(Nordvik Craft Conservatory)に留学。
・木管楽器修理をカナダの技術者Glen Wardle氏、金管楽器修理をドイツのマイスターLukas Brenner各氏に師事。
・帰国後、管楽器修理工房 高槻(当店)を立ち上げる。(岡山市中井)
・2010年 めでたく岡山が誇る繁華街、表町モール内に移転。

住所・アドレス・電話番号etc
希望イメージ
• +5 0 +5
• シンプル
複雑
• 単色
カラフル
• 暗い
明るい
• 日常
高級
• 遊び心
厳粛
• 未来的
伝統的
• 女性的
男性的
希望する色
オシャレな感じで。
納品ファイル
• 高解像度JPG (.jpg)
• イラストレーター形式 (.ai)
補足説明
700-0845
岡山県岡山市北区表町4丁目3-18 3F
TEL:086-451-7320 FAX:086-451-7321
E-mail:info@fuerepair.jp
http://www.fuerepair.jp/

A5縦長のサイズです。

http://www.fuerepair.jp/
このホームページを参考にしてください。画像等もご自由にお使いください。
ロゴ等、画像の元素材が必要な場合はご連絡下さい。
依頼公開後の追記内容
追記です。
箇条書きでなんとなく伝えてほしいことを記しましたが、文章はデザインに合うように変更してやってくださいませ。そのまま使うと稚拙な説明になってしまいますので・・・

ミントリーフオオサカのロゴを添付いたします。
「古い音楽と新しい感性の融合」のイメージです。
サイズはA5です。A6は間違いですのでお詫びして訂正いたします。

ミントリーフオオサカも管楽器専門店です。
特にサックスがメインのお店になると思います。
お店のイメージはレトロな雰囲気を目指したいと考えています。

この少ない素材、曖昧な説明でここまでのデザインが上がるとは思っておりませんでした。高級感と懐かしさを感じさせるカラーリングがとても気に入っております。

ご提案くださった皆様、誠にありがとうございました。素晴らしいデザインです。
広告費の関係で一つしか選べないことを本当に心苦しく思っております。

深く深く感謝いたしております。また次回の依頼の際もぜひともお願いいたします。

```html
<!DOCTYPE html>
<html lang="ja">
<head>
<meta charset="utf-8">
<title>ミントリーフオオサカ / 管楽器修理工房 高槻</title>
<link href="https://fonts.googleapis.com/css2?family=Noto+Sans+JP:wght@400;500;700;900&display=swap" rel="stylesheet">
<style>
  :root{
    --cream:#f3e8d2;
    --brown:#4e3219;
    --brown-light:#b08a5e;
    --blue:#3f86c4;
    --white:#fffaf0;
  }
  *{margin:0;padding:0;box-sizing:border-box}
  html,body{width:845px;height:1200px;overflow:hidden;background:var(--cream)}
  body{font-family:"Noto Sans JP",sans-serif;color:var(--brown)}
  .ad{position:relative;width:845px;height:1200px;background:linear-gradient(180deg,var(--cream) 0%,#f0e1c4 100%);overflow:hidden}

  .sax-art{position:absolute;left:0;top:140px;width:300px;height:720px;
    background:radial-gradient(ellipse at 45% 55%,rgba(176,138,94,.55) 0%,rgba(176,138,94,.25) 55%,rgba(176,138,94,0) 80%)}

  /* shop intro */
  .shop-name{position:absolute;left:28px;top:22px;width:212px;height:120px;display:flex;align-items:center;justify-content:center;
    border:3px solid var(--brown);background:var(--white);font-weight:900;font-size:25px;text-align:center;line-height:1.2}
  .opening{position:absolute;left:262px;top:22px;font-weight:700;line-height:1.25}
  .opening .place{font-size:34px;display:block}
  .opening .date{font-size:38px;display:block}
  .shop-points{position:absolute;left:262px;top:150px;list-style:none}
  .shop-points li{font-size:36px;font-weight:900;line-height:48px}
  .shop-points li::before{content:"◆";margin-right:4px}
  .web-badge{position:absolute;left:702px;top:296px;width:126px;height:126px;border-radius:50%;background:var(--blue);
    color:var(--white);display:flex;flex-direction:column;align-items:center;justify-content:center;font-weight:700;font-size:19px;line-height:1.35}
  .shop-address{position:absolute;left:262px;top:436px;font-size:16px;font-weight:700}

  /* workshop */
  .specialty-band{position:absolute;left:295px;top:476px;width:550px;height:90px;background:var(--brown);
    color:var(--white);font-size:58px;font-weight:900;letter-spacing:6px;display:flex;align-items:center;padding-left:34px}
  .services{position:absolute;left:330px;top:574px;font-size:40px;font-weight:900;letter-spacing:2px;line-height:1.3}
  .work-points{position:absolute;left:300px;top:638px;list-style:none}
  .work-points li{font-size:37px;font-weight:900;line-height:52px}
  .work-points li::before{content:"◆";margin-right:4px}

  .divider{position:absolute;left:28px;top:862px;width:789px;height:3px;background:var(--brown)}

  /* technician */
  .tech-label{position:absolute;left:28px;top:876px;width:44px;height:188px;background:var(--brown);color:var(--white);
    writing-mode:vertical-rl;font-size:21px;font-weight:700;letter-spacing:6px;display:flex;align-items:center;justify-content:center}
  .tech-career{position:absolute;left:90px;top:874px;width:496px;list-style:none;font-size:14px;font-weight:500;line-height:1.5}
  .tech-career li{margin-bottom:3px;padding-left:1em;text-indent:-1em}
  .tech-career li::before{content:"・"}
  .tech-photo{position:absolute;left:600px;top:876px;width:215px;height:158px;background:linear-gradient(160deg,#c9b08c,#8c6a45)}
  .tech-name{position:absolute;left:600px;top:1038px;width:215px;text-align:right;font-size:19px;font-weight:700;line-height:1.3}
  .tech-name small{font-size:13px;margin-right:6px;font-weight:500}

  /* footer */
  .workshop-name{position:absolute;left:28px;top:1084px;width:205px;height:76px;display:flex;align-items:center;gap:10px}
  .workshop-name .mark{width:34px;height:34px;border-radius:50%;background:var(--brown);flex:none}
  .workshop-name span{font-size:19px;font-weight:900;line-height:1.2}
  .contact{position:absolute;left:245px;top:1082px;font-size:14px;font-weight:500;line-height:1.6}
  .contact .tel{font-size:19px;font-weight:700;display:flex;align-items:center;gap:6px}
  .contact .tel .fax{font-size:14px;font-weight:500}
  .contact svg{width:17px;height:17px}
  .bottom-strip{position:absolute;left:0;top:1170px;width:845px;height:30px;background:var(--brown);color:var(--white);
    display:flex;align-items:center;justify-content:space-between;padding:0 28px;font-size:15px;font-weight:700;letter-spacing:1px}
</style>
</head>
<body>
<div class="ad">
  <div class="sax-art" role="img" aria-label="大きなサックスのイラスト"></div>

  <div class="shop-name">ミントリーフ<br>オオサカ</div>
  <p class="opening"><span class="place">新宿大久保に</span><span class="date">2012年5月オープン予定</span></p>
  <ul class="shop-points">
    <li>地下の隠れ家的楽器店</li>
    <li>リペアマン常在</li>
    <li>中古楽器買取強化実施中!</li>
    <li>委託も歓迎</li>
    <li>レアアイテムもあるよ!</li>
  </ul>
  <div class="web-badge"><span>ホームページ</span><span>近日公開</span></div>
  <p class="shop-address">〒169-0052 東京都新宿区北新宿5-8-6 リバティ西新宿ビル地下1階</p>

  <div class="specialty-band">管楽器専門店</div>
  <p class="services">修理・買取・販売</p>
  <ul class="work-points">
    <li>高い技術とお値打ちな価格</li>
    <li>特殊修理もお任せください</li>
    <li>中古・新品とも販売中</li>
    <li>どんな状態の楽器でも買取</li>
  </ul>

  <div class="divider"></div>

  <div class="tech-label">技術者紹介</div>
  <ul class="tech-career">
    <li>平成12年、高校卒業後、名古屋の専門学校で楽器修理技術を学ぶ。</li>
    <li>専門学校卒業後、ノルウェーの大学KRS(Nordvik Craft Conservatory)に留学。</li>
    <li>木管楽器修理をカナダの技術者Glen Wardle氏、金管楽器修理をドイツのマイスターLukas Brenner各氏に師事。</li>
    <li>帰国後、管楽器修理工房 高槻(当店)を立ち上げる。(岡山市中井)</li>
    <li>2010年 めでたく岡山が誇る繁華街、表町モール内に移転。</li>
  </ul>
  <div class="tech-photo" role="img" aria-label="技術者のポートレート写真"></div>
  <p class="tech-name"><small>技術者</small>高槻 悟</p>

  <div class="workshop-name"><div class="mark"></div><span>管楽器修理工房<br>高槻</span></div>
  <div class="contact">
    <p>〒700-0845 岡山県岡山市北区表町4丁目3-18 3F</p>
    <p class="tel"><svg viewBox="0 0 24 24"><path fill="currentColor" d="M6.6 10.8a15 15 0 0 0 6.6 6.6l2.2-2.2a1 1 0 0 1 1-.25 11.4 11.4 0 0 0 3.6.57 1 1 0 0 1 1 1V20a1 1 0 0 1-1 1A17 17 0 0 1 3 4a1 1 0 0 1 1-1h3.5a1 1 0 0 1 1 1c0 1.25.2 2.45.57 3.6a1 1 0 0 1-.25 1z"/></svg>TEL.086-451-7320 <span class="fax">FAX.086-451-7321</span></p>
    <p>営業時間 10:00〜19:00 定休日:火曜日(不定休あり)</p>
  </div>
  <div class="bottom-strip"><span>www.fuerepair.jp</span><span>E-mail : info@fuerepair.jp</span></div>
</div>
</body>
</html>
```